Vantrel Ashcombe LLC

we need a business card design

Industry/Entity Type

hvac

Contact Information for Business Card

my logo

Requirements
Must have
• my logo and same colors

```html
<!DOCTYPE html>
<html lang="en">
<head>
<meta charset="UTF-8">
<title>Vantrel Ashcombe LLC — Business Card</title>
<link href="https://fonts.googleapis.com/css2?family=Oswald:wght@500&family=Poppins:wght@400;700&display=swap" rel="stylesheet">
<style>
  :root {
    --backdrop: #d2d3d5;
    --brand-blue: #0862ad;
    --brand-blue-deep: #0a55a0;
    --name-blue: #0b4f9c;
    --accent-sky: #1ea0e0;
    --accent-gold: #f2a93b;
    --ink: #1f1f1f;
    --paper: #ffffff;
  }
  * { box-sizing: border-box; margin: 0; padding: 0; }
  html, body {
    width: 900px; height: 1200px; overflow: hidden;
    background: var(--backdrop);
  }
  .canvas { position: relative; width: 900px; height: 1200px; }
  .card {
    position: absolute; left: 135px; width: 630px; height: 357px;
  }
  .card-front {
    top: 214px;
    background: linear-gradient(135deg, var(--brand-blue-deep), var(--brand-blue));
  }
  .card-back { top: 628px; background: var(--paper); }

  .brand-lockup {
    position: absolute; display: flex; align-items: center; gap: 10px;
    font-family: 'Poppins', sans-serif; font-weight: 700; white-space: nowrap;
  }
  .brand-lockup .brand-dot { border-radius: 50%; flex: none; }
  .card-front .brand-lockup {
    left: 50%; top: 180px; transform: translate(-50%, -50%);
    color: var(--paper); font-size: 30px;
  }
  .card-front .brand-dot { width: 22px; height: 22px; background: var(--accent-gold); }
  .card-back .brand-lockup {
    left: 457px; top: 111px; transform: translate(-50%, -50%);
    color: var(--name-blue); font-size: 20px;
  }
  .card-back .brand-dot { width: 16px; height: 16px; background: var(--accent-gold); }

  .service-line {
    position: absolute; left: 0; right: 0; top: 312px; text-align: center;
    font-family: 'Oswald', sans-serif; font-weight: 500; font-size: 12.5px;
    color: var(--paper); letter-spacing: 0.1px; transform: scaleX(0.9);
  }

  .holder { position: absolute; left: 39px; top: 172px; }
  .holder-name {
    font-family: 'Poppins', sans-serif; font-weight: 700; font-size: 24px;
    color: var(--name-blue); line-height: 1;
  }
  .holder-role {
    font-family: 'Poppins', sans-serif; font-size: 14px; color: var(--ink);
    margin-top: 4px; line-height: 1.2;
  }
  .holder-rule { width: 49px; height: 3px; background: var(--accent-sky); margin-top: 8px; }

  .contacts { position: absolute; left: 39px; top: 247px; list-style: none; }
  .contacts li {
    display: flex; align-items: center; height: 28px;
    font-family: 'Poppins', sans-serif; font-size: 15px; color: var(--ink);
  }
  .contacts svg { width: 15px; height: 15px; margin-right: 8px; flex: none; }
  .contacts .phone-number { letter-spacing: 2px; }
</style>
</head>
<body>
<div class="canvas">
  <section class="card card-front">
    <div class="brand-lockup"><span class="brand-dot"></span>Vantrel Ashcombe LLC</div>
    <p class="service-line">FREE AC SERVICE CALLS WITH REPAIRS - SAME DAY AC REPAIRS, NEXT DAY AIR CONDITIONING INSTALLATION</p>
  </section>

  <section class="card card-back">
    <div class="brand-lockup"><span class="brand-dot"></span>Vantrel Ashcombe LLC</div>
    <div class="holder">
      <h1 class="holder-name">DORIAN PELLHAM</h1>
      <p class="holder-role">Owner</p>
      <div class="holder-rule"></div>
    </div>
    <ul class="contacts">
      <li>
        <svg viewBox="0 0 24 24" aria-hidden="true"><path fill="#f2a93b" d="M6.6 10.8a15.1 15.1 0 0 0 6.6 6.6l2.2-2.2c.3-.3.7-.4 1-.2 1.1.4 2.3.6 3.6.6.6 0 1 .4 1 1V20c0 .6-.4 1-1 1A17 17 0 0 1 3 4c0-.6.4-1 1-1h3.5c.6 0 1 .4 1 1 0 1.3.2 2.5.6 3.6.1.3 0 .7-.2 1z"/></svg>
        <span class="phone-number">555-014-2736</span>
      </li>
      <li>
        <svg viewBox="0 0 24 24" aria-hidden="true"><rect x="2" y="5" width="20" height="14" rx="1" fill="#f2a93b"/><path d="M2.5 5.5 12 13l9.5-7.5" fill="none" stroke="#fff" stroke-width="1.6"/></svg>
        <span>dorian@vantrelairco.com</span>
      </li>
      <li>
        <svg viewBox="0 0 24 24" aria-hidden="true"><g fill="none" stroke="#f2a93b" stroke-width="1.8"><circle cx="12" cy="12" r="9.5"/><ellipse cx="12" cy="12" rx="4" ry="9.5"/><path d="M2.5 12h19M4 7h16M4 17h16"/></g></svg>
        <span>vantrelashcombe.com</span>
      </li>
    </ul>
  </section>
</div>
</body>
</html>
```